Custom Home Builder Needs a Website

Harbor Stone Builders Ltd. requires a clean professional 5 page website - Home, About Us, Gallery (Interior and Exterior), Our Process and Contact Us(with registration form). We are a home builder who also has homes for sale. Also please have a place for video embedding. Editable fields by user. Using the stationery 'feel' that is attached. Need social media links. If you require any additional files, please request.

Target Market(s)

Families and professionals

Industry/Entity Type

Home Builder

Coding

Coded - Design and coding required

Number of Pages Required

5+ page

Font styles to use
Sans Serif
Other font styles liked:
• Lato

Requirements
Must have
• Editable by user
• Register Button
• Place to put home models for sale - preferably on the first page
• 5 page website -
• -Home
• -About Us
• -Gallery (Interior and Exterior)
• -Our Process
• -Contact Us.
Nice to have
• Themed similar to current stationery
• place for video embedding
• Try some darker backgrounds
• Change pictures to B/W if works for design
Should not have
• cartoonish type of content

```html
<!DOCTYPE html>
<html lang="en">
<head>
<meta charset="utf-8">
<title>Harbor Stone Builders Ltd.</title>
<link href="https://fonts.googleapis.com/css2?family=Lato:wght@400;700;900&display=swap" rel="stylesheet">
<style>
:root{
  --green:#36b300;
  --green-bright:#4dd80f;
  --green-deep:#2f9d05;
  --dark:#231f20;
  --gallery-dark:#1f1f1f;
  --ink:#111;
  --light:#eeeeee;
  --white:#fff;
  --muted:#b8b8b8;
}
*{box-sizing:border-box;margin:0;padding:0}
html,body{width:1200px;height:2628px;overflow:hidden}
body{position:relative;font-family:'Lato',Arial,sans-serif;background:var(--light);color:var(--ink)}
.abs{position:absolute}

/* Hero */
.hero{left:0;top:0;width:1200px;height:697px;
  background:linear-gradient(100deg,#cfc9c0 0%,#e9e6e1 30%,#f4f2ef 55%,#a7a9ab 72%,#e4e2de 88%,#cfcac2 100%)}
.hero-title{left:82px;top:336px;font-size:63px;font-weight:900;line-height:1.12;color:var(--ink)}
.topbar{left:0;top:0;width:1200px;height:126px;background:rgba(255,255,255,.82)}
.nav-link{top:63px;font-size:16px;font-weight:400;color:var(--ink);text-transform:uppercase}
.nav-home{left:77px;top:54px;width:91px;height:39px;background:var(--green-bright);color:var(--white);
  font-size:16px;display:flex;align-items:center;justify-content:center}
.brand{left:440px;top:44px;width:320px;text-align:center;font-size:20px;font-weight:700;color:var(--green-deep);letter-spacing:1px}
.brand small{display:block;font-size:11px;color:#555;letter-spacing:2px;font-weight:700;margin-top:2px}
.phone-top{left:955px;top:8px;display:flex;align-items:center;gap:10px;font-size:23px;font-weight:700}

/* Welcome */
.welcome{left:0;top:697px;width:1200px;height:371px;background:var(--green);
  clip-path:polygon(0 0,100% 0,100% 293px,0 371px);z-index:2}
.welcome h1{position:absolute;left:79px;top:50px;font-size:41px;font-weight:900;line-height:1.15;color:var(--white)}
.welcome p{position:absolute;left:80px;top:170px;width:560px;font-size:15.5px;line-height:1.7;color:var(--white)}
.btn-more{position:absolute;left:77px;top:273px;width:172px;height:48px;border-radius:24px;background:var(--white);
  color:var(--green);font-size:17px;display:flex;align-items:center;justify-content:center;gap:6px}
.welcome-mark{position:absolute;left:690px;top:100px;width:434px;text-align:center;font-size:62px;font-weight:900;
  color:#9be07a;line-height:1}

/* Gallery */
.gallery{left:0;top:990px;width:1200px;height:500px;
  background:radial-gradient(ellipse at 75% 30%,#3a3a3a 0%,#1d1d1d 55%,#141414 100%);z-index:1}
.section-title{position:absolute;left:0;width:1200px;text-align:center;font-size:42px;font-weight:900}
.gallery .section-title{top:100px;color:var(--white)}
.project{position:absolute;top:187px;width:235px;text-align:center;color:var(--white)}
.project .photo{width:235px;height:140px}
.project h3{font-size:25px;font-weight:900;margin-top:8px}
.project p{font-size:15.5px;line-height:1.55;margin-top:4px}
.project .more{font-size:15.5px;margin-top:5px}

/* Process */
.process{left:0;top:1486px;width:1200px;height:485px;
  background:linear-gradient(180deg,#4fc22a 0%,#3eb81c 45%,#2f9e12 100%);
  clip-path:polygon(0 0,100% 0,100% 380px,0 485px);z-index:2}
.process .section-title{top:46px;color:var(--white)}
.process-line{position:absolute;left:0;top:0}
.step{position:absolute;top:144px;width:260px;text-align:center;color:var(--white)}
.step .circle{width:131px;height:131px;border-radius:50%;margin:0 auto;border:5px solid var(--green-bright)}
.step .circle.dark{border-color:#111}
.step h3{font-size:23px;font-weight:700;margin-top:22px}
.step p{font-size:15.5px;line-height:1.55;margin-top:6px}

/* Contact */
.contact{left:0;top:1866px;width:1200px;height:446px;background:var(--light);z-index:1}
.contact .section-title{top:146px;color:var(--ink)}
.contact .section-title span{color:var(--green)}
.field{position:absolute;background:var(--white);border:1px solid #ddd;font-size:14px;color:#888;padding:14px 22px}
.submit{position:absolute;left:459px;top:341px;width:625px;height:53px;background:var(--green);color:var(--white);
  font-size:21px;font-weight:900;display:flex;align-items:center;justify-content:center}

/* Footer */
.footer{left:0;top:2312px;width:1200px;height:316px;background:var(--dark);color:var(--muted)}
.info{position:absolute;top:32px;width:300px;text-align:center;font-size:15.5px;line-height:1.45}
.info .icon{width:63px;height:63px;border-radius:50%;border:1.5px solid #8a8a8a;margin:0 auto 20px;
  display:flex;align-items:center;justify-content:center}
.rule{position:absolute;left:77px;top:169px;width:1044px;height:1px;background:#4a4647}
.social{position:absolute;top:190px;width:63px;height:63px;border-radius:50%;border:1.5px solid #8a8a8a}
.social.active{background:var(--green);border-color:var(--green)}
.copyright{position:absolute;left:0;top:272px;width:1200px;text-align:center;font-size:15px;color:var(--white)}
.copyright b{font-weight:900}
</style>
</head>
<body>

<section class="abs hero" role="img" aria-label="Photo of a bright modern kitchen with granite island, white cabinets and stainless fridge"></section>
<h2 class="abs hero-title" style="z-index:3">HARBOR STONE<br>BUILDERS LTD.</h2>

<header class="abs topbar" style="z-index:4">
  <div class="abs phone-top">
    <svg width="22" height="22" viewBox="0 0 24 24"><path fill="#36b300" d="M6.6 10.8a15 15 0 0 0 6.6 6.6l2.2-2.2a1 1 0 0 1 1-.25 11.4 11.4 0 0 0 3.6.57 1 1 0 0 1 1 1V20a1 1 0 0 1-1 1A17 17 0 0 1 3 4a1 1 0 0 1 1-1h3.5a1 1 0 0 1 1 1c0 1.25.2 2.45.57 3.57a1 1 0 0 1-.25 1z"/></svg>
    306-555-0148
  </div>
  <div class="abs nav-home">HOME</div>
  <div class="abs nav-link" style="left:201px">About Us</div>
  <div class="abs nav-link" style="left:315px">Gallery</div>
  <div class="abs brand">HARBOR STONE BUILDERS<small>LTD</small></div>
  <div class="abs nav-link" style="left:830px">Our Process</div>
  <div class="abs nav-link" style="left:1018px">Contact Us</div>
</header>

<section class="abs welcome">
  <h1>WELCOME TO<br>HARBOR STONE BUILDERS LTD.</h1>
  <p>Lorem Ipsum is simply dummy text of the printing and typesetting industry. Lorem Ipsum has been the industry's standard dummy text ever since the 1500s, when an unknown printer took a galley of type and scrambled it to...</p>
  <div class="btn-more">READ MORE <span>&#187;</span></div>
  <div class="welcome-mark">HARBOR STONE</div>
</section>

<section class="abs gallery">
  <h2 class="section-title">PROJECTS GALLERY</h2>
  <article class="project" style="left:77px">
    <div class="photo" role="img" aria-label="Photo of a two-storey house exterior" style="background:linear-gradient(180deg,#c9ced3 0%,#8c8a86 55%,#d8d8d6 100%)"></div>
    <h3>TITLE</h3><p>Lorem Ipsum is simply dummy text of the printing...</p><div class="more">READ MORE &#187;</div>
  </article>
  <article class="project" style="left:347px">
    <div class="photo" role="img" aria-label="Photo of a kitchen with mosaic backsplash" style="background:linear-gradient(180deg,#8b8682 0%,#b4aea6 60%,#6f6b67 100%)"></div>
    <h3>TITLE</h3><p>Lorem Ipsum is simply dummy text of the printing...</p><div class="more">READ MORE &#187;</div>
  </article>
  <article class="project" style="left:618px">
    <div class="photo" role="img" aria-label="Photo of a bungalow with double garage" style="background:linear-gradient(180deg,#a9c3dc 0%,#6d6257 55%,#8c8c88 100%)"></div>
    <h3>TITLE</h3><p>Lorem Ipsum is simply dummy text of the printing...</p><div class="more">READ MORE &#187;</div>
  </article>
  <article class="project" style="left:888px">
    <div class="photo" role="img" aria-label="Photo of a bright bathroom with white vanity" style="background:linear-gradient(180deg,#e4e1dc 0%,#cfcac3 60%,#9a948c 100%)"></div>
    <h3>TITLE</h3><p>Lorem Ipsum is simply dummy text of the printing...</p><div class="more">READ MORE &#187;</div>
  </article>
</section>

<section class="abs process" role="region" aria-label="Our process">
  <div class="abs" role="img" aria-label="Green-tinted photo of a house roofline and trees" style="left:0;top:120px;width:1200px;height:365px;background:linear-gradient(180deg,rgba(30,110,10,0) 0%,rgba(30,110,10,.35) 100%)"></div>
  <svg class="process-line" width="1200" height="485" viewBox="0 0 1200 485" aria-hidden="true">
    <path d="M0 170 C120 160 200 220 330 215 C460 210 560 190 700 200 C850 212 950 170 1050 175 C1120 180 1160 230 1200 270" fill="none" stroke="#ffffff" stroke-opacity=".7" stroke-width="2" stroke-dasharray="8 7"/>
  </svg>
  <h2 class="section-title">OUR&nbsp; PROCESS</h2>
  <div class="step" style="left:68px"><div class="circle dark" role="img" aria-label="Photo of a hand holding a phone" style="background:linear-gradient(135deg,#d9d6d2,#6a6864)"></div><h3>Lorem Ipsum</h3><p>Lorem Ipsum is simply dummy text of the printing and type...</p></div>
  <div class="step" style="left:336px"><div class="circle" role="img" aria-label="Photo of a planning meeting over documents" style="background:linear-gradient(135deg,#f1f1f1,#8b96a6)"></div><h3>Lorem Ipsum</h3><p>Lorem Ipsum is simply dummy text of the printing and type...</p></div>
  <div class="step" style="left:604px"><div class="circle" role="img" aria-label="Photo of a house under construction" style="background:linear-gradient(180deg,#7fa9dc,#a39a8c)"></div><h3>Lorem Ipsum</h3><p>Lorem Ipsum is simply dummy text of the printing and type...</p></div>
  <div class="step" style="left:874px"><div class="circle" role="img" aria-label="Photo of a finished home" style="background:linear-gradient(180deg,#c8d6e4,#5d5954)"></div><h3>Lorem Ipsum</h3><p>Lorem Ipsum is simply dummy text of the printing and type...</p></div>
</section>

<section class="abs contact">
  <h2 class="section-title">CONTACT <span>US</span></h2>
  <div class="field" style="left:116px;top:217px;width:332px;height:51px">Name</div>
  <div class="field" style="left:116px;top:280px;width:332px;height:51px">E - Mail</div>
  <div class="field" style="left:116px;top:341px;width:332px;height:53px">Phone</div>
  <div class="field" style="left:459px;top:217px;width:625px;height:114px">Message</div>
  <div class="submit">SUBMIT</div>
</section>

<footer class="abs footer">
  <div class="info" style="left:39px">
    <div class="icon"><svg width="22" height="26" viewBox="0 0 24 28"><path d="M12 2a8 8 0 0 0-8 8c0 6 8 15 8 15s8-9 8-15a8 8 0 0 0-8-8z" fill="none" stroke="#36b300" stroke-width="2.4"/><circle cx="12" cy="10" r="3" fill="#36b300"/></svg></div>
    PO Box 214<br>Lakeview, SK, S0K 2T0
  </div>
  <div class="info" style="left:314px">
    <div class="icon"><svg width="24" height="24" viewBox="0 0 24 24"><path fill="#36b300" d="M6.6 10.8a15 15 0 0 0 6.6 6.6l2.2-2.2a1 1 0 0 1 1-.25 11.4 11.4 0 0 0 3.6.57 1 1 0 0 1 1 1V20a1 1 0 0 1-1 1A17 17 0 0 1 3 4a1 1 0 0 1 1-1h3.5a1 1 0 0 1 1 1c0 1.25.2 2.45.57 3.57a1 1 0 0 1-.25 1z"/></svg></div>
    306-555-0148
  </div>
  <div class="info" style="left:584px">
    <div class="icon"><svg width="28" height="20" viewBox="0 0 28 20"><rect x="1.5" y="1.5" width="25" height="17" fill="none" stroke="#36b300" stroke-width="2.4"/><path d="M2 2l12 9 12-9" fill="none" stroke="#36b300" stroke-width="2.4"/></svg></div>
    Dana@harborstonebuilders.ca
  </div>
  <div class="info" style="left:854px">
    <div class="icon"><svg width="22" height="22" viewBox="0 0 24 24"><circle cx="12" cy="12" r="10" fill="none" stroke="#36b300" stroke-width="2.2"/><ellipse cx="12" cy="12" rx="4.5" ry="10" fill="none" stroke="#36b300" stroke-width="2"/><path d="M2 12h20M4 7h16M4 17h16" stroke="#36b300" stroke-width="1.8"/></svg></div>
    www.harborstonebuilders.ca
  </div>
  <div class="rule"></div>
  <a class="social active" style="left:463px" aria-label="Social network profile 1"></a>
  <a class="social" style="left:568px" aria-label="Social network profile 2"></a>
  <a class="social" style="left:675px" aria-label="Social network profile 3"></a>
  <div class="copyright">&copy; <b>HARBOR STONE BUILDERS LTD.</b> - 2016. All Rights Reserved.</div>
</footer>

</body>
</html>
```